vQ CARELINE (Brochure Design)

i need a proffesional brochure made. we are a mobile medical service company providing mobile Arterial Blood Gases(ABG's). Respiratory & Ventilator Consultation services. Ventilator and Tracheostomy training courses. and mobile vaccine administration.

this is my first time making a brochure so any and all advice/guidance will be appreciated.

i am thinking prints will be 8.5 inches x 11 inches (TRI-FOLD and BI-FOLD)

i have uploaded my business card design and logo design for reference.
as this brochure project continues ill update needs of the project descriptions.

Introduction: At vq CARELINE, we're dedicated to enhancing healthcare services by providing exceptional mobile arterial blood gases, respiratory and ventilator consultation services. Our core values revolve around excellence, compassion and accessibility. We believe that every individual deserves the highest standard of care, and we're committed to delivering that through expert guidance and top-notch training courses. Your health is at the heart of what we do, and we're here to support you on your journey to better respiratory health.

Mobile Arterial Blood Gases : Our mobile Arterial Blood Gas service offers quick, on-the-spot analysis of pH, oxygen, and carbon dioxide levels in your the blood. This service enables rapid adjustments to treatment plans for more effective respiratory care.

Ventilator and Tracheostomy Training: Our ventilator and tracheostomy course empowers caregivers and healthcare professionals to manage ventilators and care for tracheostomy patients with expertise. This training enhances patient safety, treatment outcomes, and healthcare provider confidence. vQ Careline your choice for top-notch care, convenience, and peace of mind.

Respiratory Consulting: Our respiratory consulting services provide expert guidance and support for individuals with respiratory / ventilator concerns. Benefits include personalized treatment plans, better management of respiratory conditions, and improved overall lung health. vQ Careline is your trusted partner for a breath of fresh air.

Target Market(s)

Sub-Acute facilities, Pulmonary Clinics, Pulmonologists, Nurses, Caregivers, Hospice and homehealth companies.

Industry/Entity Type

Medical; Respiratory; Nursing

Requirements
Must have
• proffesional simple design.

```html
<!DOCTYPE html>
<html lang="en">
<head>
<meta charset="utf-8">
<title>vQ CARELINE Tri-Fold Brochure</title>
<link href="https://fonts.googleapis.com/css2?family=Questrial&family=Jost:wght@600;700&display=swap" rel="stylesheet">
<style>
  :root {
    --green: #22a84a;
    --blue: #0a6bbf;
    --brand-blue: #1662c0;
    --white: #ffffff;
    --grey-text: #555a5e;
    --photo-light: #e4ebf2;
    --photo-mid: #b9c7d6;
    --photo-warm: #c9a998;
  }
  * { margin: 0; padding: 0; box-sizing: border-box; }
  html, body { width: 1200px; height: 927px; overflow: hidden; background: var(--white); }
  .brochure { position: relative; width: 1200px; height: 927px; font-family: "Questrial", sans-serif; }
  .panel { position: absolute; top: 0; height: 927px; width: 400px; overflow: hidden; }
  .panel-about { left: 0; width: 399px; background: var(--green); }
  .panel-contact { left: 399px; background: var(--white); }
  .panel-cover { left: 800px; background: var(--green); }
  .panel svg.shape { position: absolute; left: 0; top: 0; }

  .about-title {
    position: absolute; left: 30px; top: 290px;
    font-family: "Jost", sans-serif; font-weight: 700; font-size: 31px;
    color: var(--white); letter-spacing: 0.5px;
  }
  .about-text {
    position: absolute; left: 30px; top: 344px; width: 339px;
    font-size: 16.6px; line-height: 20px; color: var(--white);
    text-align: justify;
  }

  .brand-mark {
    position: absolute; display: flex; align-items: center; gap: 14px;
  }
  .brand-mark .square { display: block; }
  .brand-mark .name { font-size: 30px; letter-spacing: 0.5px; white-space: nowrap; }
  .brand-contact { left: 62px; top: 316px; }
  .brand-contact .square { width: 40px; height: 40px; background: var(--brand-blue); }
  .brand-contact .name { color: var(--brand-blue); }
  .brand-cover { left: 44px; top: 546px; }
  .brand-cover .square { width: 46px; height: 46px; background: var(--white); }
  .brand-cover .name { color: var(--white); font-size: 36px; }

  .contact-title {
    position: absolute; left: 0; width: 400px; top: 461px; text-align: center;
    font-family: "Jost", sans-serif; font-weight: 700; font-size: 22px;
    color: var(--grey-text); letter-spacing: 0.5px;
  }
  .contact-list {
    position: absolute; left: 0; width: 400px; top: 525px; list-style: none;
    text-align: center; font-size: 18.5px; line-height: 27.5px; color: var(--grey-text);
  }

  .services { position: absolute; left: 30px; top: 682px; list-style: none; }
  .service { display: flex; align-items: center; height: 80px; margin-bottom: 0; }
  .service svg { width: 60px; height: 60px; flex: none; }
  .service span { margin-left: 9px; font-size: 25.5px; color: var(--white); white-space: nowrap; }
</style>
</head>
<body>
<div class="brochure">

  <section class="panel panel-about">
    <svg class="shape" width="399" height="927" viewBox="0 0 399 927">
      <defs>
        <linearGradient id="ward-photo" x1="0" y1="0" x2="1" y2="1">
          <stop offset="0" stop-color="#4b3a4a"/>
          <stop offset="0.45" stop-color="#a7aebc"/>
          <stop offset="1" stop-color="#3f5a8c"/>
        </linearGradient>
        <linearGradient id="sample-photo" x1="0" y1="0" x2="1" y2="1">
          <stop offset="0" stop-color="#5b6478"/>
          <stop offset="0.5" stop-color="#e9e6e2"/>
          <stop offset="1" stop-color="#9fd6cf"/>
        </linearGradient>
      </defs>
      <path role="img" aria-label="Nurse adjusting a ventilator beside a patient in bed" d="M0 0 H399 V184 Q250 280 110 240 Q40 220 0 181 Z" fill="url(#ward-photo)"/>
      <path role="img" aria-label="Gloved hands drawing an arterial blood sample with a syringe" d="M0 835 Q160 640 399 709 V927 H0 Z" fill="url(#sample-photo)"/>
    </svg>
    <h2 class="about-title">ABOUT US</h2>
    <p class="about-text">At vq CARELINE, we're dedicated to enhancing healthcare services by providing exceptional mobile arterial blood gases, respiratory and ventilator consultation services. Our core values revolve around excellence, compassion and accessibility. We believe that every individual deserves the highest standard of care, and we're committed to delivering that through expert guidance and top-notch training courses. Your health is at the heart of what we do, and we're here to support you on your journey to better respiratory health.</p>
  </section>

  <section class="panel panel-contact">
    <div class="brand-mark brand-contact"><span class="square"></span><span class="name">vQ CARELINE</span></div>
    <h2 class="contact-title">CONTACT US</h2>
    <ul class="contact-list">
      <li>555.014.2290</li>
      <li>info@vqcarelinegroup.com</li>
      <li>vqcarelinegroup.com</li>
    </ul>
  </section>

  <section class="panel panel-cover">
    <svg class="shape" width="400" height="927" viewBox="0 0 400 927">
      <defs>
        <linearGradient id="bed-photo" x1="0" y1="0" x2="1" y2="1">
          <stop offset="0" stop-color="#f2f5f8"/>
          <stop offset="0.55" stop-color="#cdd9e6"/>
          <stop offset="1" stop-color="#8fa6c4"/>
        </linearGradient>
      </defs>
      <rect x="0" y="0" width="400" height="654" fill="var(--blue)"/>
      <path role="img" aria-label="Patient resting in a hospital bed connected to a ventilator while a nurse looks on" d="M0 0 H400 V456 Q300 500 200 470 Q70 430 0 322 Z" fill="url(#bed-photo)"/>
    </svg>
    <div class="brand-mark brand-cover"><span class="square"></span><span class="name">vQ CARELINE</span></div>
    <ul class="services">
      <li class="service">
        <svg viewBox="0 0 60 60" fill="none" stroke="#fff" stroke-width="2"><circle cx="30" cy="30" r="28.5"/><path d="M16 44 L22 38 M21 39 L36 24 L41 29 L26 44 Z M38 22 L43 27 M40 20 L45 25" stroke-linecap="round"/></svg>
        <span>In-house ABG’s</span>
      </li>
      <li class="service">
        <svg viewBox="0 0 60 60" fill="none" stroke="#fff" stroke-width="2"><circle cx="30" cy="30" r="28.5"/><rect x="19" y="14" width="20" height="16" rx="1.5"/><path d="M23 26 L26 20 L29 25 L32 19 L35 26"/><rect x="21" y="32" width="16" height="8"/><path d="M24 40 V46 M34 40 V46 M20 47 H38 M37 36 H44 V42"/></svg>
        <span>Ventilator Training</span>
      </li>
      <li class="service">
        <svg viewBox="0 0 60 60" fill="none" stroke="#fff" stroke-width="2"><circle cx="30" cy="30" r="28.5"/><path d="M30 14 V30 M30 28 L26 32 M30 28 L34 32"/><path d="M26 24 C20 22 15 32 16 42 C17 46 22 45 26 42 Z" fill="#fff"/><path d="M34 24 C40 22 45 32 44 42 C43 46 38 45 34 42 Z" fill="#fff"/></svg>
        <span>Respiratory Consulting</span>
      </li>
    </ul>
  </section>

</div>
</body>
</html>
```